Save The Date for 2019 RLX Colloquium

We have an annual meeting each June and need a Save the Date (STD) designed. It should be a two-sided postcard with room for address and stamp (according to US Mail postal standards). I have attached some examples from prior years, but we would appreciate a more modern and attractive design for this year's STD.

Target Market(s)

Our own members - nurses, nurse practitioners, PAs and physicians

Industry/Entity Type

Medical

Requirements
Must have
• Must include our logos (attached), ideally in a coordinating fashion - as was done in prior years (see examples attached) and without modifying the logos too much. Needs have the following information:
• - "Save the Date"
• - "The 12th Annual Heartline Crew Colloquium"
• - "Friday, June 7, 2019" or "6/7/19"
• - "The Varrick–Dunmore Building | 318 West 57th Street | NYC"
• - Please include our website (www.qb-zrh.org/events), phone number (212-555-0147) and email address (ask@qb-zrh.org) for people to ask questions
• - Must have space for a postage stamp and the name/address of the postcard recipient
Nice to have
• Would be nice to remain in our blue/grey/olive color palate (see attached Brand Standards guide).
Should not have
• Please do not use stock photos of medical staff. Please don't use cartoons or cartoon images (although a tasteful sketch may be considered).

```html
<!DOCTYPE html>
<html lang="en">
<head>
<meta charset="utf-8">
<title>Save the Date – 2019 RLX Colloquium</title>
<link href="https://fonts.googleapis.com/css2?family=Montserrat:wght@400;600;700;800&family=Nunito+Sans:wght@300;400;700;800&family=Libre+Caslon+Text:wght@400;700&display=swap" rel="stylesheet">
<style>
  :root{
    --bg:#9b9b9b;
    --navy:#0d2d6b;
    --blue:#0f4c9c;
    --blue-deep:#0a2f73;
    --olive:#ada27a;
    --olive-dark:#9a8f64;
    --white:#ffffff;
    --ink:#14306b;
    --link:#1f5aa8;
  }
  *{box-sizing:border-box;margin:0;padding:0}
  html,body{width:1200px;height:1200px;overflow:hidden}
  body{background:var(--bg);font-family:"Nunito Sans",sans-serif;position:relative}

  .card{position:absolute;left:252px;width:696px;height:544px;background:var(--white);box-shadow:0 6px 14px rgba(0,0,0,.35)}
  .card--front{top:53px}
  .card--back{top:602px}

  /* front */
  .hero{position:absolute;left:14px;top:14px;width:669px;height:410px;border-radius:26px 26px 0 0;overflow:hidden;
    background:radial-gradient(ellipse at 40% 35%, #1a5cb4 0%, var(--blue) 45%, var(--blue-deep) 100%)}
  .hero__art{position:absolute;left:422px;top:20px;width:244px;height:380px;border-radius:45% 40% 50% 50%;
    background:radial-gradient(ellipse at 45% 40%, #c5d4ef 0%, #7f9fd7 40%, #2e63b8 80%, rgba(15,76,156,0) 100%)}
  .hero__pulse{position:absolute;left:0;bottom:30px;width:669px;height:70px}
  .tab{position:absolute;left:193px;top:14px;width:311px;height:46px}
  .tab__label{position:absolute;left:0;top:16px;width:696px;text-align:center;font-family:"Montserrat",sans-serif;font-weight:700;
    font-size:24px;letter-spacing:3.5px;color:var(--navy)}
  .headline{position:absolute;left:49px;top:117px;color:var(--white)}
  .headline__kicker{font-family:"Montserrat",sans-serif;font-weight:400;font-size:26px;line-height:1}
  .headline__kicker sup{font-size:14px;vertical-align:10px}
  .headline__title{font-family:"Montserrat",sans-serif;font-weight:700;font-size:41px;line-height:.98;color:var(--olive);margin-top:8px;letter-spacing:-.3px}
  .headline__date{font-family:"Montserrat",sans-serif;font-weight:400;font-size:27px;margin-top:8px}
  .venue{position:absolute;left:48px;top:283px;color:var(--white);font-size:18px;line-height:1.25}
  .venue__row{display:flex;align-items:flex-start;gap:7px;margin-bottom:10px}
  .venue__name{font-weight:800;font-family:"Montserrat",sans-serif;font-size:17px}
  .icon{flex:none;width:21px;height:21px;margin-top:1px}
  .venue__web b{font-weight:800}

  .info-bar{position:absolute;left:0;top:424px;width:696px;height:29px;background:var(--olive);color:var(--white);
    display:flex;align-items:center;padding-left:53px;gap:10px;font-size:18px}
  .info-bar__label{font-weight:300;letter-spacing:.5px;margin-right:4px}
  .info-bar__item{display:flex;align-items:center;gap:6px;font-weight:800;font-family:"Montserrat",sans-serif;font-size:17px}
  .info-bar .icon{width:18px;height:18px;margin:0}

  .partners{position:absolute;left:0;top:453px;width:696px;height:91px;display:flex;align-items:center;padding-left:32px}
  .partner{display:flex;align-items:center;gap:10px;color:var(--link);font-size:11px;line-height:1.35;letter-spacing:.3px}
  .partner__mark{width:50px;height:50px;border-radius:50%;border:2px solid var(--link);flex:none}
  .partner__lead{font-style:italic;font-size:10px}
  .partner--1{width:206px}
  .partner--2{width:238px}

  /* back */
  .sender{position:absolute;left:36px;top:34px;display:flex}
  .sender__mark{width:80px;height:80px;border-radius:50%;border:3px solid var(--navy);flex:none}
  .sender__rule{width:1px;height:86px;background:var(--navy);margin:12px 17px 0 15px}
  .sender__name{font-family:"Libre Caslon Text",serif;color:var(--navy);font-size:28px;line-height:1;margin-top:16px}
  .sender__sub{font-family:"Libre Caslon Text",serif;font-weight:700;color:var(--navy);font-size:13px;margin-top:8px}
  .sender__addr{color:var(--navy);font-size:14px;line-height:1.15;margin-top:6px}

  .invite{position:absolute;left:0;top:140px;width:333px;height:334px;background:var(--blue);color:var(--white);overflow:hidden}
  .invite__body{position:absolute;left:36px;top:26px;width:278px;font-size:13.3px;line-height:1.27;text-align:justify}
  .invite__body p{margin-bottom:10px}
  .invite__body b{font-weight:800}
  .questions{position:absolute;left:0;bottom:0;width:333px;height:52px}
  .questions__tab{position:absolute;left:0;top:0;width:160px;height:24px;background:var(--olive);clip-path:polygon(0 0,84% 0,100% 100%,0 100%)}
  .questions__bar{position:absolute;left:0;top:23px;width:333px;height:29px;background:var(--olive)}
  .questions__label{position:absolute;left:36px;top:4px;font-size:16px;font-weight:300;color:var(--white);letter-spacing:.4px}
  .questions__row{position:absolute;left:36px;top:28px;display:flex;gap:12px;color:var(--white);font-family:"Montserrat",sans-serif;font-weight:700;font-size:15px}
  .questions__row span{display:flex;align-items:center;gap:5px}
  .questions .icon{width:17px;height:17px;margin:0}
  .lodging{position:absolute;left:36px;top:484px;color:var(--navy);font-size:13.5px;line-height:1.2}
  .lodging b{font-weight:800}
</style>
</head>
<body>

<section class="card card--front">
  <div class="hero">
    <svg class="hero__pulse" viewBox="0 0 669 70" aria-hidden="true"><polyline fill="none" stroke="#2b6bc4" stroke-width="1.5" points="0,45 120,45 135,30 145,60 160,5 175,50 190,45 330,45 345,35 355,55 368,10 382,48 395,45 560,45 575,30 585,60 600,8 615,50 669,45"/></svg>
    <div class="hero__art" role="img" aria-label="Anatomical illustration of a human heart in blue tones"></div>
  </div>
  <svg class="tab" viewBox="0 0 311 46" aria-hidden="true"><path d="M0 0 H311 L285 36 Q278 46 266 46 H45 Q33 46 26 36 Z" fill="#fff"/></svg>
  <div class="tab__label">SAVE THE DATE</div>

  <div class="headline">
    <div class="headline__kicker">THE 12<sup>TH</sup> ANNUAL</div>
    <div class="headline__title">HEARTLINE CREW<br>COLLOQUIUM</div>
    <div class="headline__date">FRIDAY, JUNE 7, 2019</div>
  </div>

  <div class="venue">
    <div class="venue__row">
      <svg class="icon" viewBox="0 0 22 22" aria-hidden="true"><circle cx="11" cy="11" r="10" fill="none" stroke="#fff" stroke-width="1.4"/><path d="M5.5 11 L11 6 L16.5 11 M7.5 10 V16 H14.5 V10" fill="none" stroke="#fff" stroke-width="1.6"/></svg>
      <div><div class="venue__name">The Varrick–Dunmore Building</div><div>318 West 57th Street | NYC</div></div>
    </div>
    <div class="venue__row venue__web">
      <svg class="icon" viewBox="0 0 22 22" aria-hidden="true"><circle cx="11" cy="11" r="10" fill="none" stroke="#fff" stroke-width="1.4"/><path d="M8 6 L15 12 L11.5 12.5 L13.5 16.5 L12 17 L10 13 L8 15 Z" fill="#fff"/></svg>
      <div>www.<b>qb-zrh</b>.org/events</div>
    </div>
  </div>

  <div class="info-bar">
    <span class="info-bar__label">FOR ADDITIONAL INFORMATION</span>
    <span class="info-bar__item"><svg class="icon" viewBox="0 0 22 22" aria-hidden="true"><circle cx="11" cy="11" r="10" fill="none" stroke="#14306b" stroke-width="1.6"/><path d="M7.5 6.5 L9.5 6 L10.5 8.8 L9.3 9.8 Q10.4 12.4 12.4 13.6 L13.4 12.4 L16 13.4 L15.6 15.4 Q10 15.8 7.5 6.5 Z" fill="#14306b"/></svg>212-555-0147</span>
    <span class="info-bar__item"><svg class="icon" viewBox="0 0 22 22" aria-hidden="true"><circle cx="11" cy="11" r="10" fill="none" stroke="#14306b" stroke-width="1.6"/><rect x="6" y="7.5" width="10" height="7" fill="none" stroke="#14306b" stroke-width="1.4"/><path d="M6 7.5 L11 11.5 L16 7.5" fill="none" stroke="#14306b" stroke-width="1.4"/></svg>ask@qb-zrh.org</span>
  </div>

  <div class="partners">
    <div class="partner partner--1"><span class="partner__mark"></span><div><div class="partner__lead">Presented by</div>The Harbor Heart<br>Society, Inc.</div></div>
    <div class="partner partner--2"><span class="partner__mark"></span><div><div class="partner__lead">of the</div>Empire Chapter,<br>Qorvane Board of Cardiology</div></div>
    <div class="partner"><span class="partner__mark"></span><div><div class="partner__lead">In Association with</div>Halden Cardiac Center</div></div>
  </div>
</section>

<section class="card card--back">
  <div class="sender">
    <span class="sender__mark"></span>
    <span class="sender__rule"></span>
    <div>
      <div class="sender__name">Empire State</div>
      <div class="sender__sub">CHAPTER</div>
      <div class="sender__addr">742 9th Avenue, Ste. 1410<br>New York, NY 10019</div>
    </div>
  </div>

  <div class="invite">
    <div class="invite__body">
      <p>Join us for TWO great events at Linwood Golf Club in the Rochester area this June!</p>
      <p>On June 1st, <b>The Annual Heartline Crew (RLX) Colloquium,</b> a unique all-day academic event designed to enhance current knowledge about the etiology, prevention, intervention and management of cardiovascular disease that’s now in its 11th year, will take place at the Linwood Golf Club in Pittsford, NY.</p>
      <p>Following the RLX Colloquium, the Empire Chapter of the QBC will host <b>The Second Annual Summer Soirée</b> for all members and friends of QBZRH. Be sure to save the date!</p>
    </div>
    <div class="questions">
      <div class="questions__tab"></div>
      <div class="questions__bar"></div>
      <div class="questions__label">QUESTIONS?</div>
      <div class="questions__row">
        <span><svg class="icon" viewBox="0 0 22 22" aria-hidden="true"><circle cx="11" cy="11" r="10" fill="none" stroke="#14306b" stroke-width="1.6"/><path d="M7.5 6.5 L9.5 6 L10.5 8.8 L9.3 9.8 Q10.4 12.4 12.4 13.6 L13.4 12.4 L16 13.4 L15.6 15.4 Q10 15.8 7.5 6.5 Z" fill="#14306b"/></svg>212-555-0147</span>
        <span><svg class="icon" viewBox="0 0 22 22" aria-hidden="true"><circle cx="11" cy="11" r="10" fill="none" stroke="#14306b" stroke-width="1.6"/><rect x="6" y="7.5" width="10" height="7" fill="none" stroke="#14306b" stroke-width="1.4"/><path d="M6 7.5 L11 11.5 L16 7.5" fill="none" stroke="#14306b" stroke-width="1.4"/></svg>ask@qb-zrh.org</span>
      </div>
    </div>
  </div>

  <div class="lodging"><b>Recommended lodging:</b> The Ashgrove Lodge<br>Rochester Hotel &amp; Spa</div>
</section>

</body>
</html>
```